Casa Vero Inspections Business Card

I need a business card for my new company. The company is going to provide home inspections. The name of the company is Casa Vero Inspections. I am not sure if I want a single sided card or a double. I have a logo already that I want to incorporate into the card design. I was wondering if I should incorporate a catch phrase on my card or not. If I did the phrase would be "The Intelligent Choice for Home Inspections" but i am unsure how or if to use it on a card. The following information needs to be on the card.
Home Inspection
My Name: Marcus T. Wolford Phone Number: 555-301-7762 Email: mwolford@casaveroinspections.com Website: www.casaveroinspections.com NY HI License # 27300519462

```html
<!DOCTYPE html>
<html lang="en">
<head>
<meta charset="UTF-8">
<title>Casa Vero Inspections — Business Card</title>
<link rel="stylesheet" href="https://fonts.googleapis.com/css2?family=Open+Sans:wght@400;700&display=swap">
<style>
  :root {
    --brand-blue: #0b74b8;
    --brand-blue-deep: #075f99;
    --accent-blue: #7fc0e8;
    --paper: #f6f7f8;
    --ink-white: #ffffff;
    --stage: #e6e8eb;
  }
  * { box-sizing: border-box; margin: 0; padding: 0; }
  html, body {
    width: 1200px; height: 900px; overflow: hidden;
    background: var(--stage);
    font-family: "Open Sans", Arial, sans-serif;
  }
  .sheet {
    width: 1200px; height: 900px;
    display: flex; flex-direction: column;
    align-items: center; justify-content: center; gap: 40px;
  }
  .card {
    width: 700px; height: 400px;
    position: relative; overflow: hidden;
    box-shadow: 0 6px 18px rgba(0,0,0,0.18);
  }

  /* Front */
  .card-front { display: flex; background: var(--paper); }
  .front-panel {
    width: 400px; height: 100%;
    background: var(--brand-blue);
    color: var(--ink-white);
    padding: 52px 0 0 44px;
    position: relative;
  }
  .holder-name {
    font-weight: 700; font-size: 22px; letter-spacing: 0.5px;
    text-transform: uppercase;
  }
  .contact-list {
    list-style: none;
    position: absolute; left: 44px; bottom: 46px;
    font-size: 15px; line-height: 24px;
  }
  .contact-list li { display: flex; align-items: center; gap: 10px; }
  .contact-list svg { width: 14px; height: 14px; flex: none; }
  .contact-list .license { padding-left: 0; }
  .accent-stripe {
    width: 10px; height: 100%;
    margin-left: 14px;
    background: var(--accent-blue);
  }
  .front-brand {
    flex: 1; display: flex; align-items: center; justify-content: center;
    gap: 10px; padding-right: 10px;
  }
  .brand-mark { width: 14px; height: 14px; background: var(--brand-blue); flex: none; }
  .brand-name {
    font-weight: 700; font-size: 22px; line-height: 1.15;
    color: var(--brand-blue); text-align: left;
  }

  /* Back */
  .card-back {
    background: linear-gradient(135deg, var(--brand-blue) 0%, var(--brand-blue) 55%, var(--brand-blue-deep) 100%);
    display: flex; align-items: center; justify-content: center; gap: 14px;
  }
  .card-back .brand-mark { width: 18px; height: 18px; background: var(--ink-white); }
  .card-back .brand-name { color: var(--ink-white); font-size: 34px; }
</style>
</head>
<body>
<main class="sheet">
  <section class="card card-front" aria-label="Card front">
    <div class="front-panel">
      <h1 class="holder-name">Marcus T. Wolford</h1>
      <ul class="contact-list">
        <li>
          <svg viewBox="0 0 16 16" aria-hidden="true"><path fill="#fff" d="M3.6 1.5l2.3 2.6-1.3 1.6c.9 2 2.6 3.7 4.6 4.6l1.6-1.3 2.6 2.3-1.4 2.2C6.8 13.2 2.8 9.2 1.4 3z"/></svg>
          555-301-7762
        </li>
        <li>
          <svg viewBox="0 0 16 16" aria-hidden="true"><rect x="1" y="3.5" width="14" height="9" fill="#fff"/><path d="M1.5 4l6.5 5 6.5-5" fill="none" stroke="#0b74b8" stroke-width="1.4"/></svg>
          mwolford@casaveroinspections.com
        </li>
        <li>
          <svg viewBox="0 0 16 16" aria-hidden="true"><g fill="none" stroke="#fff" stroke-width="1.3"><circle cx="8" cy="8" r="6.5"/><ellipse cx="8" cy="8" rx="2.8" ry="6.5"/><path d="M1.5 8h13"/></g></svg>
          www.casaveroinspections.com
        </li>
        <li class="license">NY HI License # 27300519462</li>
      </ul>
    </div>
    <div class="accent-stripe"></div>
    <div class="front-brand">
      <span class="brand-mark"></span>
      <p class="brand-name">Casa Vero Inspections</p>
    </div>
  </section>

  <section class="card card-back" aria-label="Card back">
    <span class="brand-mark"></span>
    <p class="brand-name">Casa Vero Inspections</p>
  </section>
</main>
</body>
</html>
```